Valbrook Data Works

Our company is about IT hardwares and IT solutions. IT hardware such as PC, RAMS, storage and servers. IT solutions such as project management, BA. We are also selling new technology too.

Target Market(s)

Consumer, Small to Medium Business, Corporate

Requirements
Must have
• The business card must have the following:
• Name:
• Title:
• Contact Number:
• Email address:
• Website:
• Color: Must match the logo color upgrade

```html
<!DOCTYPE html>
<html lang="en">
<head>
<meta charset="utf-8">
<title>Valbrook Data Works — Business Card</title>
<link rel="stylesheet" href="https://fonts.googleapis.com/css2?family=Roboto:wght@400;500;700&display=swap">
<style>
  :root {
    --backdrop: #2e2a27;
    --card: #1c1f23;
    --card-edge: #121417;
    --gold: #e0922c;
    --muted: #6a6d72;
    --white: #f3f3f3;
    --divider: #4a4d52;
  }
  * { margin: 0; padding: 0; box-sizing: border-box; }
  html, body {
    width: 1200px; height: 769px; overflow: hidden;
    background: var(--backdrop);
    font-family: "Roboto", Arial, sans-serif;
  }
  .stage { position: relative; width: 1200px; height: 769px; }
  .card {
    position: absolute; width: 520px; height: 297px;
    background: var(--card);
    border-radius: 3px;
    box-shadow: 0 14px 30px rgba(0,0,0,.45), 0 0 0 1px var(--card-edge);
  }
  .card--front { left: 70px; top: 110px; }
  .card--back { left: 610px; top: 362px; }

  .wordmark {
    display: flex; align-items: center; gap: 10px;
    color: var(--gold); font-weight: 700; text-transform: uppercase;
    letter-spacing: 1px; font-size: 22px; line-height: 1;
  }
  .wordmark__dot {
    width: 12px; height: 12px; background: var(--gold); flex: none;
  }
  .card--front .wordmark {
    position: absolute; left: 0; right: 0; top: 118px; justify-content: center;
  }
  .card--front .website {
    position: absolute; left: 0; right: 0; top: 176px; text-align: center;
    color: var(--white); font-size: 13px; letter-spacing: 4px; opacity: .85;
  }

  .card--back .wordmark {
    position: absolute; left: 28px; top: 136px; font-size: 17px; gap: 8px;
  }
  .card--back .wordmark__dot { width: 10px; height: 10px; }
  .divider {
    position: absolute; left: 290px; top: 78px; width: 1px; height: 142px;
    background: var(--divider);
  }
  .contact { position: absolute; left: 312px; top: 96px; }
  .contact__name {
    color: var(--gold); font-weight: 700; font-size: 19px; text-transform: uppercase;
  }
  .contact__title {
    color: var(--white); font-weight: 500; font-size: 14px; text-transform: uppercase;
    margin-top: 2px; margin-bottom: 16px;
  }
  .contact__line {
    display: flex; align-items: center; gap: 8px;
    color: var(--white); font-size: 13px; margin-bottom: 5px;
  }
  .contact__line svg { width: 11px; height: 11px; flex: none; fill: var(--gold); }
</style>
</head>
<body>
<div class="stage">
  <section class="card card--front">
    <div class="wordmark"><span class="wordmark__dot"></span>Valbrook Data Works</div>
    <div class="website">www.valbrookdata.com</div>
  </section>

  <section class="card card--back">
    <div class="wordmark"><span class="wordmark__dot"></span>Valbrook Data Works</div>
    <div class="divider"></div>
    <div class="contact">
      <div class="contact__name">Marcus Hale</div>
      <div class="contact__title">CEO/Founder</div>
      <div class="contact__line">
        <svg viewBox="0 0 24 24"><path d="M6.6 10.8a15 15 0 0 0 6.6 6.6l2.2-2.2a1 1 0 0 1 1-.25 11.4 11.4 0 0 0 3.6.57 1 1 0 0 1 1 1V20a1 1 0 0 1-1 1A17 17 0 0 1 3 4a1 1 0 0 1 1-1h3.5a1 1 0 0 1 1 1c0 1.25.2 2.45.57 3.57a1 1 0 0 1-.25 1z"/></svg>
        555 214 7390
      </div>
      <div class="contact__line">
        <svg viewBox="0 0 24 24"><path d="M2 5h20v14H2z M2 5l10 8 10-8" /></svg>
        marcus@valbrookdata.com
      </div>
      <div class="contact__line">
        <svg viewBox="0 0 24 24"><circle cx="12" cy="12" r="10"/></svg>
        www.valbrookdata.com
      </div>
    </div>
  </section>
</div>
</body>
</html>
```